4 Banners for homepage and logo

Logo for SiteTitleCounsel.net and 4 banners for the center of the page.

Logo should be clean and pretty basic.

Banners
1.
Domain Name Disputes
We'll recover your domain names, Guaranteed or its free!

2.
Reputation management
We get defamatory content removed from Quarvo, Bramz, Chirplet, and Pagewall!

3.
Domain name management
Create an offensive or defensive domain name strategy for your company

4.
Defensive reputation management
Get ahead of the game and make your image shine online!

```html
<!DOCTYPE html>
<html lang="en">
<head>
<meta charset="utf-8">
<title>SiteTitleCounsel.net – Homepage Banners</title>
<link rel="stylesheet" href="https://fonts.googleapis.com/css2?family=Open+Sans:ital,wght@0,700;1,800&family=Questrial&display=swap">
<style>
  :root {
    --page-bg: #ffffff;
    --logo-teal: #1b8fa3;
    --title-teal: #1e7f92;
    --tagline-green: #78b41c;
    --panel-light: #eef0f0;
    --panel-navy: #10297a;
    --panel-blue: #2650bd;
    --tone-blue-soft: #b9cfe8;
    --tone-paper: #e2e2df;
    --tone-grey: #d4d6d7;
    --white: #ffffff;
  }
  * { box-sizing: border-box; margin: 0; padding: 0; }
  html, body {
    width: 1200px; height: 900px; overflow: hidden;
    background: var(--page-bg);
  }
  .canvas { position: relative; width: 1200px; height: 900px; }

  .site-logo {
    position: absolute; left: 58px; top: 62px;
    font-family: "Questrial", sans-serif;
    font-size: 58px; font-weight: 400; letter-spacing: -0.5px;
    color: var(--logo-teal);
  }

  .banner {
    position: absolute; width: 584px; height: 254px;
    background: var(--panel-light); overflow: hidden;
  }
  .banner--disputes   { left: 10px;  top: 206px; }
  .banner--reputation { left: 606px; top: 206px; }
  .banner--management { left: 10px;  top: 472px; height: 250px; }
  .banner--defensive  { left: 606px; top: 472px; height: 250px; background: var(--panel-navy); }

  .banner-photo { position: absolute; top: 0; bottom: 0; right: 0; width: 60%; }
  .photo--globe { background: linear-gradient(90deg, var(--panel-light) 0%, var(--tone-blue-soft) 100%); }
  .photo--paper { background: linear-gradient(90deg, var(--panel-light) 0%, var(--tone-paper) 100%); }
  .photo--www   { background: linear-gradient(90deg, var(--panel-light) 0%, var(--tone-grey) 100%); }
  .photo--earth { background: linear-gradient(90deg, var(--panel-navy) 0%, var(--panel-blue) 100%); }

  .banner-copy { position: relative; z-index: 1; padding: 34px 0 0 34px; }
  .banner-title {
    font-family: "Open Sans", sans-serif; font-weight: 700;
    font-size: 36px; line-height: 44px; color: var(--title-teal);
    letter-spacing: -0.3px;
  }
  .banner-tagline {
    margin-top: 18px;
    font-family: "Open Sans", sans-serif; font-weight: 800; font-style: italic;
    font-size: 22px; line-height: 32px; color: var(--tagline-green);
  }
  .banner--defensive .banner-title,
  .banner--defensive .banner-tagline { color: var(--white); }
  .banner--defensive .banner-copy { padding-top: 30px; }
</style>
</head>
<body>
<main class="canvas">
  <header class="site-logo">SiteTitleCounsel.net</header>

  <section class="banner banner--disputes">
    <div class="banner-photo photo--globe" role="img" aria-label="Photo of a globe with a browser address bar and pointer"></div>
    <div class="banner-copy">
      <h2 class="banner-title">Domain Name<br>Disputes</h2>
      <p class="banner-tagline">We'll recover your domain<br>names, Guaranteed or its<br>free! »</p>
    </div>
  </section>

  <section class="banner banner--reputation">
    <div class="banner-photo photo--paper" role="img" aria-label="Photo of a signed legal document"></div>
    <div class="banner-copy">
      <h2 class="banner-title">Reputation<br>Management</h2>
      <p class="banner-tagline">We get defamatory content<br>removed from Quarvo, Bramz,<br>Chirplet, and Pagewall! »</p>
    </div>
  </section>

  <section class="banner banner--management">
    <div class="banner-photo photo--www" role="img" aria-label="Photo of a blurred web address"></div>
    <div class="banner-copy">
      <h2 class="banner-title">Domain Name<br>Management</h2>
      <p class="banner-tagline">Create an offensive or<br>defensive domain name<br>strategy for your company »</p>
    </div>
  </section>

  <section class="banner banner--defensive">
    <div class="banner-photo photo--earth" role="img" aria-label="Photo of the earth glowing on a blue background"></div>
    <div class="banner-copy">
      <h2 class="banner-title">Defensive Reputation<br>Management</h2>
      <p class="banner-tagline">Get ahead of the game and<br>make your image shine<br>online! »</p>
    </div>
  </section>
</main>
</body>
</html>
```